Burn Cream

We need to develop a (1) tube and (2) carton design. For a Lidocaine 2.5% burn cream.

This is a topical application cream. VALTIQ is the Product Name. 1 oz.

Product

```html
<!DOCTYPE html>
<html lang="en">
<head>
<meta charset="utf-8">
<title>VALTIQ Burn Cream – Tube Label</title>
<link rel="stylesheet" href="https://fonts.googleapis.com/css2?family=Montserrat:wght@400;500&display=swap">
<style>
  :root {
    --page: #ffffff;
    --navy-deep: #0c1640;
    --navy: #1b2a66;
    --navy-glow: #2b4fb3;
    --flame-red: #e2481c;
    --flame-orange: #f39a16;
    --flame-yellow: #ffd21f;
    --ice-light: #e8f4fb;
    --ice-blue: #8fc3e6;
    --ice-deep: #2f6fc4;
    --ring-gold: #f2b632;
    --label-white: #ffffff;
    --band: rgba(255, 255, 255, 0.28);
  }
  * { box-sizing: border-box; margin: 0; padding: 0; }
  html, body {
    width: 1200px;
    height: 784px;
    overflow: hidden;
    background: var(--page);
  }
  .canvas {
    position: relative;
    width: 1200px;
    height: 784px;
  }
  .tube-label {
    position: absolute;
    left: 100px;
    top: 212px;
    width: 1000px;
    height: 360px;
    overflow: hidden;
    background:
      radial-gradient(ellipse 420px 300px at 760px 180px, var(--navy-glow) 0%, rgba(43, 79, 179, 0) 70%),
      linear-gradient(180deg, var(--navy) 0%, var(--navy-deep) 100%);
  }
  .flame-art {
    position: absolute;
    left: 120px;
    top: 40px;
    width: 360px;
    height: 280px;
    border-radius: 0 140px 140px 0;
    background: linear-gradient(90deg,
      rgba(255, 210, 31, 0) 0%,
      var(--flame-yellow) 30%,
      var(--flame-orange) 70%,
      var(--flame-red) 100%);
  }
  .ice-art {
    position: absolute;
    right: 0;
    top: 0;
    width: 300px;
    height: 360px;
    background: linear-gradient(90deg,
      rgba(143, 195, 230, 0) 0%,
      var(--ice-blue) 40%,
      var(--ice-light) 100%);
  }
  .brand-mark {
    position: absolute;
    left: 370px;
    top: 50px;
    width: 260px;
    height: 260px;
    border-radius: 50%;
    border: 6px solid var(--ring-gold);
    background: var(--navy-deep);
  }
  .brand-text {
    position: absolute;
    left: 50%;
    top: 50%;
    transform: translate(-50%, -50%) rotate(-90deg);
    display: flex;
    flex-direction: column;
    align-items: flex-start;
    font-family: "Montserrat", sans-serif;
    color: var(--label-white);
    white-space: nowrap;
  }
  .strength {
    font-size: 14px;
    font-weight: 400;
    letter-spacing: 0.5px;
    margin-bottom: 2px;
  }
  .product-name {
    font-size: 56px;
    font-weight: 500;
    letter-spacing: 2px;
    line-height: 1;
  }
  .light-band {
    position: absolute;
    left: 0;
    right: 0;
    top: 290px;
    height: 16px;
    background: var(--band);
  }
</style>
</head>
<body>
  <main class="canvas">
    <section class="tube-label">
      <div class="flame-art" role="img" aria-label="Illustration of yellow and orange flames"></div>
      <div class="ice-art" role="img" aria-label="Illustration of shattered ice cubes with blue sparkles"></div>
      <div class="light-band"></div>
      <div class="brand-mark">
        <div class="brand-text">
          <span class="strength">Lidocaine 2.5%</span>
          <span class="product-name">VALTIQ</span>
        </div>
      </div>
    </section>
  </main>
</body>
</html>
```